Meadowlark Crate Society - New Website Design

Create a professional website for strawberries of the month club; a subscription box business that will INCLUDE dipped strawberries - some with sprinkles. Check out: http://www.plumvine.com for examples. Our website URL will be www.MeadowlarkCrateSociety.com
Please see quillpouch.com; toffeeguild.com and gruffcase.com for the concept I am after. The business has not been launched yet, I am currently in the pre-launch stage using a specialized landing page website, and so the time scale for developing my professional looking website is up to 1-2 weeks.
The webpage should have a fun feel and should match the style of the company logo at toffeeguild.com or gruffcase.com. The pages to include are 'Home', 'About us' and 'Get Started'
Thank you and good luck!

```html
<!DOCTYPE html>
<html lang="en">
<head>
<meta charset="utf-8">
<title>Get Started – Berrybloom Subs.</title>
<link href="https://fonts.googleapis.com/css2?family=Poppins:wght@400;500;600&family=Roboto:wght@400;500&display=swap" rel="stylesheet">
<style>
:root{
  --ink:#1f1f24;
  --muted:#6b6b73;
  --red:#f6485e;
  --green:#3fc07a;
  --orange:#f7a21b;
  --blush:#f8e9e9;
  --purple:#9a5cf2;
  --purple-light:#b184fb;
  --footer:#39424b;
  --footer-text:#c0c5cb;
  --line:#ececef;
}
*{box-sizing:border-box;margin:0;padding:0}
html,body{width:962px;height:1200px;overflow:hidden;background:#fff}
body{position:relative;font-family:"Roboto",sans-serif;color:var(--ink)}
.abs{position:absolute}
.heading{font-family:"Poppins",sans-serif;font-weight:400}

/* header */
.site-header{left:0;top:0;width:962px;height:72px;border-bottom:1px solid var(--line)}
.nav{left:70px;top:30px;display:flex;gap:29px;font-family:"Poppins",sans-serif;font-size:10px;font-weight:500;letter-spacing:.2px}
.nav a{color:var(--ink);text-decoration:none}
.nav a.active{color:var(--red)}
.nav-bar{left:206px;top:0;width:63px;height:2px;background:var(--red)}
.brand{left:375px;top:24px;display:flex;align-items:center;gap:9px;font-family:"Poppins",sans-serif;font-weight:600;font-size:18px;color:#8c8c94}
.brand-dot{width:22px;height:22px;border-radius:50%;background:var(--red)}
.header-icons{left:794px;top:28px;display:flex;gap:18px}
.cart-badge{left:876px;top:27px;width:9px;height:9px;border-radius:50%;background:var(--red);color:#fff;font-size:6px;text-align:center;line-height:9px}

/* hero */
.hero{left:0;top:72px;width:962px;height:184px;background:var(--blush)}
.hero-title{left:0;top:136px;width:962px;text-align:center;font-size:26px;font-weight:500;font-family:"Poppins",sans-serif}
.crumbs{left:0;top:175px;width:962px;text-align:center;font-size:10px;word-spacing:1px}
.crumbs span{margin:0 10px}
.down-btn{left:463px;top:238px;width:36px;height:36px;border-radius:50%;background:#fff;box-shadow:0 4px 12px rgba(0,0,0,.08);display:flex;align-items:center;justify-content:center}

/* plans */
.rule{left:465px;top:306px;width:32px;height:1px;background:#d8d8dc}
.section-title{left:0;top:312px;width:962px;text-align:center;font-size:23px;font-weight:400}
.section-sub{left:0;top:350px;width:962px;text-align:center;font-size:11.5px;color:var(--muted)}
.plan{border:1px solid var(--line);background:#fff;text-align:center}
.plan-name{font-family:"Poppins",sans-serif;font-size:16px;margin-top:28px}
.price{font-family:"Poppins",sans-serif;font-weight:600;font-size:26px;line-height:1.1;margin-top:2px}
.price small{font-weight:400;font-size:15px;color:#9a9aa2}
.ship{font-size:9px;margin-top:4px;letter-spacing:.2px}
.plan-photo{margin:12px auto 0;width:150px;height:126px;border-radius:8px}
.btn{display:inline-block;font-family:"Roboto",sans-serif;font-weight:500;font-size:10px;border-radius:22px;letter-spacing:.2px}
.btn-outline{width:110px;height:36px;line-height:34px;border:1.5px solid #e6e6ea;color:var(--ink);margin-top:16px}
.btn-fill{width:122px;height:39px;line-height:39px;background:var(--red);color:#fff;margin-top:17px;box-shadow:0 6px 14px rgba(246,72,94,.3)}
.tagline{left:0;top:766px;width:962px;text-align:center;font-size:14.5px;color:var(--muted);font-weight:400}

/* newsletter + footer */
.footer-shape{left:0;top:870px}
.newsletter{left:133px;top:835px;width:695px;height:89px;border-radius:45px;background:var(--purple);box-shadow:0 10px 24px rgba(120,60,220,.25)}
.nl-title{left:40px;top:31px;font-family:"Poppins",sans-serif;font-size:19px;font-weight:500;color:#fff}
.nl-field{left:178px;top:27px;width:370px;height:35px;border-radius:18px;background:var(--purple-light);display:flex;align-items:center;gap:8px;padding-left:15px;font-size:10.5px;color:#fff}
.nl-submit{left:564px;top:27px;width:98px;height:35px;border-radius:18px;background:#fff;font-size:9.5px;font-weight:500;text-align:center;line-height:35px}
.foot-h{font-family:"Poppins",sans-serif;font-size:15px;color:#fff;top:970px}
.foot-list{list-style:none;font-size:10px;color:var(--footer-text)}
.foot-list li{height:28.5px;display:flex;align-items:flex-start;gap:7px}
.ico{width:9px;height:9px;border-radius:50%;flex:none;margin-top:2px}
.ico-red{background:var(--red)}
.ico-soc{background:#fff}
.foot-list li.hl{color:var(--red)}
.foot-rule{left:70px;top:1150px;width:822px;height:1px;background:#46505a}
.copyright{left:0;top:1170px;width:962px;text-align:center;font-size:10px;color:#fff}
.to-top{left:912px;top:1138px;width:29px;height:29px;border-radius:50%;background:#fff;display:flex;align-items:center;justify-content:center}
</style>
</head>
<body>

<header class="site-header abs">
  <div class="nav-bar abs"></div>
  <nav class="nav abs"><a href="#">HOME</a><a href="#">ABOUT US</a><a href="#" class="active">GET STARTED</a></nav>
  <div class="brand abs"><span class="brand-dot"></span>Berrybloom Subs.</div>
  <div class="header-icons abs">
    <svg width="16" height="16" viewBox="0 0 16 16" fill="none" stroke="#555" stroke-width="1.4"><circle cx="6.5" cy="6.5" r="5"/><path d="M10.2 10.2L15 15"/></svg>
    <svg width="16" height="18" viewBox="0 0 16 18" fill="none" stroke="#555" stroke-width="1.4"><circle cx="8" cy="5" r="4"/><path d="M1 17c0-4 3-6 7-6s7 2 7 6z"/></svg>
    <svg width="16" height="16" viewBox="0 0 16 16" fill="none" stroke="#555" stroke-width="1.4"><path d="M1 2h2.5l2 8h8l1.5-6H5"/><circle cx="6" cy="13.5" r="1"/><circle cx="12.5" cy="13.5" r="1"/></svg>
  </div>
  <div class="cart-badge abs">1</div>
</header>

<section class="hero abs"></section>
<h1 class="hero-title abs">Get Started</h1>
<div class="crumbs abs">HOME<span>&gt;</span>GET STARTED</div>
<div class="down-btn abs"><svg width="10" height="10" viewBox="0 0 10 10" fill="none" stroke="#333" stroke-width="1.2"><path d="M5 1v8M2 6l3 3 3-3"/></svg></div>

<div class="rule abs"></div>
<h2 class="section-title heading abs">Choose your Plan</h2>
<p class="section-sub abs">Aenean leo ligula porttitor eu consequat vitae eleifend ac enim aliquam lorem ante dapibus in viverra.</p>

<article class="plan abs" style="left:72px;top:393px;width:239px;height:314px">
  <div class="plan-name">Monthly Plan</div>
  <div class="price" style="color:var(--green)">$29.99<small>/month</small></div>
  <div class="ship">(PLUS SHIPPING)</div>
  <div class="plan-photo" role="img" aria-label="Single strawberry half dipped in dark chocolate" style="background:radial-gradient(circle at 50% 40%,#e8333d 0,#c9242d 28%,#6b3a26 42%,#fff 60%)"></div>
  <a class="btn btn-outline">GET STARTED</a>
</article>

<article class="plan abs" style="left:349px;top:393px;width:264px;height:346px">
  <div class="plan-name" style="margin-top:32px;font-size:17px">6 Month Plan</div>
  <div class="price" style="color:var(--red);font-size:28px">$24.99<small style="font-size:16px">/month</small></div>
  <div class="ship">(PLUS SHIPPING)</div>
  <div class="plan-photo" role="img" aria-label="Two chocolate-covered strawberries with drizzle" style="margin-top:20px;background:radial-gradient(ellipse at 50% 55%,#5a3423 0,#3d2418 30%,#fff 62%)"></div>
  <a class="btn btn-fill">GET STARTED</a>
</article>

<article class="plan abs" style="left:650px;top:393px;width:240px;height:314px">
  <div class="plan-name">12 Month Plan</div>
  <div class="price" style="color:var(--orange)">$21.99<small>/month</small></div>
  <div class="ship">(PLUS SHIPPING)</div>
  <div class="plan-photo" role="img" aria-label="Bowl of pink and chocolate dipped strawberries with sprinkles" style="background:radial-gradient(ellipse at 50% 45%,#f39bbd 0,#8a5a4a 32%,#ece6e6 48%,#fff 62%)"></div>
  <a class="btn btn-outline">GET STARTED</a>
</article>

<p class="tagline abs">Consequat vitae eleifend ac enim aliquam lorem ante dapibus in viverra lorem ipsum.</p>

<svg class="footer-shape abs" width="962" height="330" viewBox="0 0 962 330"><path d="M0 28 Q481 -20 962 28 V330 H0Z" fill="var(--footer)"/></svg>

<div class="newsletter abs">
  <div class="nl-title abs">Newsletter</div>
  <div class="nl-field abs"><svg width="10" height="8" viewBox="0 0 10 8" fill="none" stroke="#fff" stroke-width="1"><rect x=".5" y=".5" width="9" height="7"/><path d="M.5 .5l4.5 4 4.5-4"/></svg>Enter your email address</div>
  <div class="nl-submit abs">SUBMIT</div>
</div>

<h3 class="foot-h abs" style="left:70px">Quick Links</h3>
<ul class="foot-list abs" style="left:70px;top:1006px"><li>› Home</li><li>› About us</li><li>› Get Started</li></ul>

<h3 class="foot-h abs" style="left:328px">Contact</h3>
<ul class="foot-list abs" style="left:328px;top:1006px">
  <li><span class="ico ico-red"></span>+123 555 0142</li>
  <li><span class="ico ico-red"></span>info@berrybloomsubs.com</li>
  <li style="height:auto"><span class="ico ico-red"></span>6:30am - 5:00pm PT<br>(Monday - Friday)</li>
</ul>

<h3 class="foot-h abs" style="left:661px">Follow us on socail media</h3>
<ul class="foot-list abs" style="left:661px;top:1006px">
  <li><span class="ico ico-soc"></span>Huddle</li>
  <li class="hl"><span class="ico ico-red"></span>Chirper</li>
  <li><span class="ico ico-soc"></span>Pinboardly</li>
  <li><span class="ico ico-soc"></span>Snapframe</li>
</ul>
<ul class="foot-list abs" style="left:752px;top:1006px">
  <li><span class="ico ico-soc"></span>Reelcast</li>
  <li><span class="ico ico-soc"></span>Linkfold</li>
</ul>

<div class="foot-rule abs"></div>
<p class="copyright abs">© 2017, All Rights Reserved.</p>
<div class="to-top abs"><svg width="10" height="10" viewBox="0 0 10 10" fill="none" stroke="#333" stroke-width="1.2"><path d="M5 9V1M2 4l3-3 3 3"/></svg></div>

</body>
</html>
```